Artificial Intelligence and Machine Learning Company Needs a New Website

We need a new web design for one of the leading companies in the Spanish market in the development of advanced analytics and artificial intelligence.
Our goal is to help in resolving complex planning decisions and improving the operational efficiency of our clients. We have big clients from different industries and very powerful technology partners. We want our new website to be clear and show our great experience in the sector (more than 10 years) and our young spirit.
Number of Pages Required
5+ page
Colors
Designer to choose colors to be used in the design.
Look and feel
Each slider illustrates characteristics of the customer's brand and the style your logo design should communicate.

```html
<!DOCTYPE html>
<html lang="en">
<head>
<meta charset="utf-8">
<title>Quarvo — Advanced analytics and AI</title>
<link href="https://fonts.googleapis.com/css2?family=Mulish:ital,wght@0,400;0,600;0,700;0,800;1,400&display=swap" rel="stylesheet">
<style>
:root{
  --orange:#f0451d;
  --orange-dark:#d8340f;
  --ink:#222226;
  --text:#5b5b60;
  --muted:#8d8d92;
  --grey-bg:#f1f1f2;
  --line:#dedee0;
  --dark:#16161a;
  --footer:#1b1b1f;
  --purple:#8a2a8e;
  --white:#ffffff;
}
*{box-sizing:border-box;margin:0;padding:0}
html,body{width:1200px;height:4944px;overflow:hidden}
body{font-family:"Mulish",Arial,sans-serif;color:var(--text);background:var(--white);position:relative}
.abs{position:absolute}

/* header */
.site-header{position:absolute;top:0;left:0;width:1200px;height:128px;background:var(--white)}
.brand{position:absolute;left:56px;top:40px;display:flex;align-items:center;gap:12px;font-size:40px;font-weight:800;color:var(--orange);letter-spacing:-1px}
.brand-dot{width:22px;height:22px;border-radius:50%;background:var(--orange)}
.main-nav{position:absolute;left:384px;top:58px;display:flex;gap:34px;font-size:17px;font-weight:700;color:var(--ink);text-transform:uppercase}
.main-nav .active{color:var(--orange);position:relative}
.main-nav .active::after{content:"";position:absolute;left:0;right:0;bottom:-20px;height:3px;background:var(--orange)}
.header-tools{position:absolute;right:56px;top:20px;display:flex;gap:24px}
.header-tools span{width:18px;height:18px;border-radius:50%;border:2px solid var(--muted)}

/* hero */
.hero{position:absolute;top:128px;left:0;width:1200px;height:592px;background:linear-gradient(100deg,#0d0d10 0%,#1b1715 45%,#2a1610 70%,#111 100%)}
.hero-visual{position:absolute;right:0;top:0;width:640px;height:592px;background:radial-gradient(ellipse at 60% 40%,rgba(240,69,29,.75) 0%,rgba(160,40,15,.35) 35%,rgba(0,0,0,0) 70%)}
.hero-copy{position:absolute;left:112px;top:188px;width:520px;color:var(--white)}
.hero-copy h1{font-size:34px;line-height:42px;font-weight:700}
.hero-copy p{margin-top:12px;font-size:19px;line-height:25px;font-weight:700}
.hero-copy p em{font-style:normal;color:var(--orange)}
.hero-copy .join{display:block;margin-top:22px;font-size:21px;font-weight:800;color:var(--orange)}
.dots{position:absolute;display:flex;gap:8px}
.dots i{width:12px;height:12px;border-radius:50%;background:rgba(255,255,255,.5)}
.dots i.on{background:var(--white)}

/* intro split */
.intro{position:absolute;top:720px;left:0;width:1200px;height:680px}
.intro-bg{position:absolute;left:0;top:0}
.intro-col{position:absolute;top:130px;width:440px;text-align:center}
.intro-col .ico{display:block;width:96px;height:96px;margin:0 auto}
.intro-col h2{margin-top:30px;font-size:36px;font-weight:700}
.intro-col p{margin-top:16px;font-size:16px;line-height:22px}
.intro-what{left:80px;color:var(--white)}
.intro-who{left:680px;color:var(--ink)}
.intro-who p{color:var(--muted)}
.btn-white{display:inline-block;margin-top:26px;padding:14px 34px;border-radius:28px;background:var(--white);color:var(--orange);font-weight:700;font-size:16px}

/* section titles */
.section-title{position:absolute;left:0;width:1200px;text-align:center;font-size:46px;font-weight:700;color:var(--ink)}

/* industries */
.industry{position:absolute;width:236px;height:250px;background:var(--white);box-shadow:0 2px 10px rgba(0,0,0,.1)}
.industry .photo{height:188px}
.industry .cap{height:62px;display:flex;align-items:center;justify-content:center;text-align:center;font-size:17px;font-weight:700;color:var(--ink);line-height:20px}
.industry.active{transform:translateY(-14px)}
.industry.active .cap{background:var(--orange);color:var(--white);position:relative}
.industry.active .cap::after{content:"";position:absolute;right:16px;bottom:14px;width:12px;height:12px;background:var(--white)}

/* how we work */
.how{position:absolute;top:2160px;left:0;width:1200px;height:652px;background:var(--grey-bg)}
.step{position:absolute;top:364px;width:220px}
.step h3{font-size:19px;font-weight:800;color:var(--ink)}
.step .when{margin-top:4px;font-size:14px;color:var(--orange);font-weight:700;line-height:18px}
.step .dur{font-size:14px;color:var(--muted)}
.step p{margin-top:12px;font-size:14px;line-height:20px;color:var(--muted)}

/* testimonial */
.testimonial{position:absolute;top:2812px;left:0;width:1200px;height:488px;background:linear-gradient(180deg,#2a2a2e,#111114)}
.quote{position:absolute;left:220px;top:96px;width:760px;text-align:center;color:var(--white);font-size:21px;line-height:30px}
.quote-mark{position:absolute;left:210px;top:80px;font-size:64px;color:var(--white);font-weight:800;line-height:1}
.author{position:absolute;left:0;width:1200px;top:262px;text-align:center;color:var(--white)}
.author b{display:block;font-size:18px;font-weight:800;letter-spacing:.5px}
.author span{font-size:15px;color:#c9c9cc}
.btn-orange{position:absolute;left:490px;top:360px;width:220px;height:52px;line-height:52px;border-radius:26px;background:var(--orange);color:var(--white);text-align:center;font-weight:700;font-size:17px}
.chev{position:absolute;top:206px;width:20px;height:20px;border-top:3px solid var(--white);border-left:3px solid var(--white)}

/* technologies */
.tech{position:absolute;top:3448px;width:168px;height:350px;background:var(--white);box-shadow:0 2px 12px rgba(0,0,0,.1);text-align:center;padding-top:22px}
.tech .ring{display:block;width:96px;height:96px;margin:0 auto}
.tech h3{margin-top:14px;font-size:17px;font-weight:700;color:var(--ink);line-height:21px;height:42px}
.tech p{margin:14px 14px 0;font-size:13px;line-height:18px;color:var(--muted)}
.tech .more{display:block;margin-top:16px;font-size:14px;color:var(--orange);font-weight:700}

/* clients */
.clients{position:absolute;top:3832px;left:0;width:1200px;height:168px;background:var(--orange)}
.client{position:absolute;top:64px;font-size:30px;font-weight:800;color:var(--white)}

/* contact */
.contact-item{position:absolute;top:4160px;display:flex;align-items:center;gap:16px;font-size:19px;line-height:24px;color:var(--ink)}
.contact-item .c{width:84px;height:84px}
.building{position:absolute;left:0;top:4272px;width:1200px;height:240px;background:linear-gradient(180deg,#ffffff 0%,#ececee 60%,#d9d9dc 100%)}

/* footer */
.site-footer{position:absolute;top:4512px;left:0;width:1200px;height:432px;background:var(--footer);color:#d4d4d8}
.fcol{position:absolute;top:56px}
.fcol h4{font-size:18px;font-weight:700;color:var(--white);letter-spacing:.5px;margin-bottom:22px}
.fcol li{list-style:none;font-size:15px;line-height:30px;display:flex;align-items:center;gap:10px}
.fcol li::before{content:"";width:6px;height:6px;border-radius:50%;background:var(--orange)}
.fcol.social li::before{display:none}
.fcol.social li{gap:14px;line-height:50px;font-size:17px}
.fcol.social i{width:36px;height:36px;border-radius:50%;background:var(--orange)}
.news p{font-size:15px;line-height:22px;width:300px}
.news .field{margin-top:20px;display:flex;width:300px;height:42px}
.news .field span{flex:1;background:var(--white);color:#999;font-size:14px;padding:12px}
.news .field b{width:96px;background:var(--orange);color:var(--white);font-size:13px;text-align:center;line-height:42px}
.copyright{position:absolute;left:0;bottom:0;width:1200px;height:64px;border-top:1px solid #333;text-align:center;line-height:64px;font-size:14px;color:#9a9aa0}
</style>
</head>
<body>

<header class="site-header">
  <div class="brand">Quarvo<span class="brand-dot"></span></div>
  <nav class="main-nav">
    <span class="active">Industries ▾</span><span>Technologies ▾</span><span>About us ▾</span><span>Resources</span><span>Partners</span>
  </nav>
  <div class="header-tools"><span></span><span></span><span></span><span></span></div>
</header>

<section class="hero">
  <div class="hero-visual" role="img" aria-label="Glowing orange digital brain over a dark circuit board"></div>
  <div class="hero-copy">
    <h1>Planning, optimization, decision management</h1>
    <p>Advanced analytics and <em>Artificial Intelligence</em><br>for smart decisions</p>
    <span class="join">INTERESTED TO JOIN US?</span>
  </div>
  <div class="dots" style="left:568px;top:556px"><i class="on"></i><i></i><i></i></div>
</section>

<section class="intro">
  <svg class="intro-bg" width="1200" height="680" viewBox="0 0 1200 680">
    <polygon points="600,0 1200,0 1200,600 600,680" fill="#f4f4f5"/>
    <polygon points="0,0 600,0 600,680 0,600" fill="#f0451d"/>
    <polygon points="0,0 600,0 600,80" fill="#e63e17" opacity=".6"/>
  </svg>
  <div class="intro-col intro-what">
    <svg class="ico" viewBox="0 0 96 96" fill="none" stroke="#fff" stroke-width="3"><circle cx="48" cy="48" r="14"/><circle cx="48" cy="12" r="6"/><circle cx="84" cy="48" r="6"/><circle cx="48" cy="84" r="6"/><circle cx="12" cy="48" r="6"/><path d="M48 18v16M78 48H62M48 78V62M18 48h16"/></svg>
    <h2>What We Do</h2>
    <p>Sed metus augue commodo at vehicula ut pulvinar eu ante. Integer nec tellus finibus vitae consequat nec porta vel lectus. Nulla sit amet elementum enim. Proin cursus tempor.</p>
    <span class="btn-white">Learn More</span>
  </div>
  <div class="intro-col intro-who">
    <svg class="ico" viewBox="0 0 96 96" fill="none" stroke="#444" stroke-width="3"><rect x="16" y="20" width="64" height="44" rx="3"/><path d="M36 76h24M48 64v12"/><rect x="34" y="32" width="28" height="20"/></svg>
    <h2>Who We Are</h2>
    <p>Sed metus augue commodo at vehicula ut pulvinar eu ante. Integer nec tellus finibus vitae consequat nec porta vel lectus. Nulla sit amet elementum enim. Proin cursus tempor.</p>
  </div>
</section>

<h2 class="section-title" style="top:1400px">Areas &amp; Industries</h2>

<div class="industry" style="left:108px;top:1520px"><div class="photo" role="img" aria-label="Field technician at work" style="background:linear-gradient(135deg,#7d8a96,#3f4a55)"></div><div class="cap">Field Services</div></div>
<div class="industry active" style="left:356px;top:1520px"><div class="photo" role="img" aria-label="Insurance advisers meeting" style="background:linear-gradient(135deg,#c4b8ad,#6f6258)"></div><div class="cap">Insurance</div></div>
<div class="industry" style="left:604px;top:1520px"><div class="photo" role="img" aria-label="Warehouse shelves with boxes" style="background:linear-gradient(135deg,#b9a48a,#6a5640)"></div><div class="cap">Transportation<br>&amp; logistics</div></div>
<div class="industry" style="left:852px;top:1520px"><div class="photo" role="img" aria-label="Workers reviewing a schedule" style="background:linear-gradient(135deg,#c7ccd2,#7b8590)"></div><div class="cap">Workforce Planning</div></div>
<div class="industry" style="left:108px;top:1808px"><div class="photo" role="img" aria-label="Welding sparks on a production line" style="background:linear-gradient(135deg,#5a6470,#d58a3a)"></div><div class="cap">Manufacturing</div></div>
<div class="industry" style="left:356px;top:1808px"><div class="photo" role="img" aria-label="Jet engine detail" style="background:linear-gradient(135deg,#a9b4be,#4d5863)"></div><div class="cap">Aviation</div></div>
<div class="industry" style="left:604px;top:1808px"><div class="photo" role="img" aria-label="Retail store aisle" style="background:linear-gradient(135deg,#d2c3a8,#8a7357)"></div><div class="cap">Retail</div></div>
<div class="industry" style="left:852px;top:1808px"><div class="photo" role="img" aria-label="Bank office team" style="background:linear-gradient(135deg,#b4a594,#5d5148)"></div><div class="cap">Banking</div></div>

<section class="how">
  <h2 class="section-title" style="top:70px">How We Work</h2>
  <svg class="abs" style="left:0;top:180px" width="1200" height="140" viewBox="0 0 1200 140">
    <line x1="236" y1="62" x2="968" y2="62" stroke="#cfcfd3" stroke-width="2"/>
    <g fill="#8a2a8e"><circle cx="312" cy="62" r="5"/><circle cx="576" cy="62" r="5"/><circle cx="840" cy="62" r="5"/></g>
    <g fill="#fff" stroke="#f0451d" stroke-width="7">
      <circle cx="180" cy="62" r="52"/><circle cx="444" cy="62" r="52"/><circle cx="708" cy="62" r="52"/><circle cx="972" cy="62" r="52"/>
    </g>
    <g fill="none" stroke="#333" stroke-width="2.5">
      <rect x="162" y="42" width="36" height="40" rx="2"/><path d="M170 72v-8M178 72v-14M186 72v-10"/>
      <circle cx="438" cy="56" r="14"/><path d="M448 66l12 12"/><rect x="432" y="50" width="12" height="12"/>
      <rect x="690" y="44" width="36" height="36" rx="3"/><circle cx="708" cy="62" r="8"/>
      <path d="M972 38c10 8 12 22 8 34h-16c-4-12-2-26 8-34zM964 72l-6 10M980 72l6 10"/><circle cx="972" cy="56" r="4"/>
    </g>
  </svg>
  <div class="step" style="left:112px"><h3>Initial analysis</h3><div class="when">Time of Change</div><div class="dur">0.5 - 1 day</div><p>Sed ut perspiciatis unde omnis iste natus error sit voluptatem accusantium doloremque laudantium totam rem aperiam.</p></div>
  <div class="step" style="left:376px"><h3>Scan</h3><div class="when">We only Change 50%</div><div class="dur">2 - 3 days</div><p>Sed ut perspiciatis unde omnis iste natus error sit voluptatem accusantium doloremque laudantium totam rem aperiam.</p></div>
  <div class="step" style="left:640px"><h3>Prototype</h3><div class="when">We only Change 75%</div><div class="dur">5 - 15 days</div><p>Sed ut perspiciatis unde omnis iste natus error sit voluptatem accusantium doloremque laudantium totam rem aperiam.</p></div>
  <div class="step" style="left:904px"><h3>Project</h3><p>Sed ut perspiciatis unde omnis iste natus error sit voluptatem accusantium doloremque laudantium totam rem aperiam.</p></div>
</section>

<section class="testimonial" role="img" aria-label="Dark background of hands typing on a keyboard">
  <span class="quote-mark">“</span>
  <p class="quote">Curabitur iaculis tempus eros. Curabitur vel mi sit amet magna malesuada ultricies ut in nisl fermentum vel congue et euismod in. Fusce ultricies orci ac feugiat suscipit leo massa sodales velit et scelerisque ex tortor at ipsum. Proin orci odio commodo in gravida nec.</p>
  <div class="author"><b>LUCAS FERRER ORTIZ</b><span>Head of Operations, Department of R&amp;D</span></div>
  <span class="btn-orange">Success Stories</span>
  <div class="dots" style="left:570px;top:448px"><i></i><i class="on"></i><i></i></div>
  <span class="chev" style="left:104px;transform:rotate(-45deg)"></span>
  <span class="chev" style="left:1074px;transform:rotate(135deg)"></span>
</section>

<h2 class="section-title" style="top:3364px">Technologies</h2>

<div class="tech" style="left:41px"><svg class="ring" viewBox="0 0 96 96" fill="none"><circle cx="48" cy="48" r="44" stroke="#f0451d" stroke-width="4"/><g stroke="#333" stroke-width="2.5"><path d="M28 64V40M40 64V32M52 64V46M64 64V36"/><path d="M24 66h48"/></g></svg><h3>Advanced<br>Analytics</h3><p>Find out how we use prediction and prescription analytics to improve business performance.</p><span class="more">Learn How »</span></div>
<div class="tech" style="left:231px"><svg class="ring" viewBox="0 0 96 96" fill="none"><circle cx="48" cy="48" r="44" stroke="#f0451d" stroke-width="4"/><g stroke="#333" stroke-width="2.5"><circle cx="48" cy="44" r="16"/><path d="M40 60v10h16V60M48 28v32"/></g></svg><h3>Artificial<br>Intelligence</h3><p>Find out how we use prediction and prescription analytics to improve business performance.</p><span class="more">Learn How »</span></div>
<div class="tech" style="left:421px"><svg class="ring" viewBox="0 0 96 96" fill="none"><circle cx="48" cy="48" r="44" stroke="#f0451d" stroke-width="4"/><g stroke="#333" stroke-width="2.5"><circle cx="34" cy="36" r="8"/><circle cx="62" cy="36" r="8"/><circle cx="48" cy="62" r="8"/><path d="M42 36h12M38 43l6 12M58 43l-6 12"/></g></svg><h3>Rule-based<br>systems</h3><p>Find out how we use prediction and prescription analytics to improve business performance.</p><span class="more">Learn How »</span></div>
<div class="tech" style="left:611px"><svg class="ring" viewBox="0 0 96 96" fill="none"><circle cx="48" cy="48" r="44" stroke="#f0451d" stroke-width="4"/><g stroke="#333" stroke-width="2.5"><circle cx="48" cy="48" r="12"/><path d="M48 28v8M48 60v8M28 48h8M60 48h8M34 34l6 6M56 56l6 6M62 34l-6 6M34 62l6-6"/></g></svg><h3>Machine<br>learning</h3><p>Find out how we use prediction and prescription analytics to improve business performance.</p><span class="more">Learn How »</span></div>
<div class="tech" style="left:801px"><svg class="ring" viewBox="0 0 96 96" fill="none"><circle cx="48" cy="48" r="44" stroke="#f0451d" stroke-width="4"/><g stroke="#333" stroke-width="2.5"><rect x="32" y="26" width="32" height="44" rx="3"/><path d="M38 36h20M38 46h8M50 46h8M38 56h8M50 56h8"/></g></svg><h3>Mathematical<br>Optimization</h3><p>Find out how we use prediction and prescription analytics to improve business performance.</p><span class="more">Learn How »</span></div>
<div class="tech" style="left:991px"><svg class="ring" viewBox="0 0 96 96" fill="none"><circle cx="48" cy="48" r="44" stroke="#f0451d" stroke-width="4"/><g stroke="#333" stroke-width="2.5"><rect x="28" y="30" width="16" height="16"/><rect x="52" y="30" width="16" height="16"/><rect x="40" y="54" width="16" height="16"/><path d="M44 38h8M36 46l8 8M60 46l-8 8"/></g></svg><h3>Flexible<br>Architecture</h3><p>Find out how we use prediction and prescription analytics to improve business performance.</p><span class="more">Learn How »</span></div>

<section class="clients">
  <span class="chev" style="left:28px;top:74px;transform:rotate(-45deg)"></span>
  <span class="client" style="left:110px">Trevanor</span>
  <span class="client" style="left:330px">Mercalo</span>
  <span class="client" style="left:545px">Brunhal</span>
  <span class="client" style="left:745px">Avialta</span>
  <span class="client" style="left:960px">Redelvo</span>
</section>

<h2 class="section-title" style="top:4040px">Contact Us</h2>

<div class="contact-item" style="left:196px"><svg class="c" viewBox="0 0 84 84" fill="none"><circle cx="42" cy="42" r="39" stroke="#f0451d" stroke-width="4"/><rect x="26" y="30" width="32" height="24" rx="2" stroke="#f0451d" stroke-width="2.5"/><path d="M26 32l16 12 16-12" stroke="#f0451d" stroke-width="2.5"/></svg><span>Information<br>Request</span></div>
<div class="contact-item" style="left:510px"><svg class="c" viewBox="0 0 84 84" fill="none"><circle cx="42" cy="42" r="39" stroke="#f0451d" stroke-width="4"/><rect x="26" y="28" width="32" height="22" rx="2" stroke="#f0451d" stroke-width="2.5"/><path d="M34 58h16M42 50v8" stroke="#f0451d" stroke-width="2.5"/></svg><span>Ask for a<br>Demo</span></div>
<div class="contact-item" style="left:800px"><svg class="c" viewBox="0 0 84 84" fill="none"><circle cx="42" cy="42" r="39" stroke="#f0451d" stroke-width="4"/><path d="M26 46v-6a16 16 0 0132 0v6" stroke="#f0451d" stroke-width="2.5"/><rect x="24" y="44" width="8" height="12" rx="2" stroke="#f0451d" stroke-width="2.5"/><rect x="52" y="44" width="8" height="12" rx="2" stroke="#f0451d" stroke-width="2.5"/></svg><span>Let us give<br>you a call</span></div>

<div class="building" role="img" aria-label="Light line sketch of a modern office building"></div>

<footer class="site-footer">
  <div class="fcol" style="left:80px"><h4>QUICK LINKS</h4><ul><li>Home</li><li>Industries</li><li>Technologies</li><li>About Us</li><li>Resources</li><li>Partners</li></ul></div>
  <div class="fcol" style="left:330px"><h4>HOW WE WORK</h4><ul><li>Initial analysis</li><li>Scan</li><li>Prototype</li><li>Project</li></ul></div>
  <div class="fcol news" style="left:560px"><h4>SUBSCRIBE THE NEWSLETTER</h4><p>Lorem ipsum dolor sit amet, consectetur adipiscing.</p><div class="field"><span>Email Address</span><b>SUBSCRIBE</b></div></div>
  <div class="fcol social" style="left:940px"><h4>FOLLOW US</h4><ul><li><i></i>Circlr</li><li><i></i>Chirper</li><li><i></i>Photoly</li></ul></div>
  <div class="copyright">© 2019 Quarvo Analytics | All rights reserved.</div>
</footer>

</body>
</html>
```